Business Card & Stationary for Cleaning Company
Business Card, Letterhead, Invoice, Envelope, Fax Cover, Presentation Folder (Letter)
Professional
Brightwave Home Services
Raleigh and Surround Area
Name@brightwavehomeservices.example
www.brightwavehomeservices.example
Please integrate my already-completed company logo (attached) in a clean, modern design for business cards, Fax cover sheet, letterhead, envelopes, Invoice and Presentation Folder (Letter).
Here is my company logo in ai format. Please let me know if there's another format you prefer to work with; I'll try to send that along.
This project is a guaranteed as you can see the link below for the new logo.
http://www.pixelquarry.example/contests/a-logo-for-cleaning-company

```html
<!DOCTYPE html>
<html lang="en">
<head>
<meta charset="utf-8">
<title>Brightwave Home Services – Stationery</title>
<link rel="stylesheet" href="https://fonts.googleapis.com/css2?family=Open+Sans:wght@400;600;700&display=swap">
<style>
  :root {
    --green: #8cc63f;
    --blue: #1aa3e8;
    --blue-soft: #bfe6fa;
    --ink: #3a3a3a;
    --ink-light: #ffffff;
    --paper: #ffffff;
  }
  * { box-sizing: border-box; margin: 0; padding: 0; }
  html, body { width: 1200px; height: 857px; overflow: hidden; background: var(--paper); }
  body { position: relative; font-family: "Open Sans", Arial, sans-serif; color: var(--ink); }

  .brand { display: flex; align-items: center; gap: 10px; font-weight: 700; color: var(--green); white-space: nowrap; }
  .brand-dot { border-radius: 50%; background: var(--blue); flex: none; }

  /* Business card front */
  .card-front {
    position: absolute; left: 5px; top: 5px; width: 355px; height: 206px;
    border: 10px solid var(--green); background: var(--paper);
    display: flex; align-items: center; justify-content: center;
  }
  .card-front .brand { font-size: 22px; flex-direction: column; gap: 8px; }
  .card-front .brand-dot { width: 54px; height: 54px; }

  /* Business card back */
  .card-back {
    position: absolute; left: 5px; top: 235px; width: 360px; height: 188px;
    display: flex; font-size: 8px; color: var(--ink-light);
  }
  .card-back-contact {
    width: 187px; background: var(--blue); padding: 70px 14px 0 0;
    text-align: right; line-height: 1.7;
  }
  .card-back-name { flex: 1; background: var(--green); padding: 76px 0 0 12px; line-height: 2.4; }

  /* Envelope */
  .envelope { position: absolute; left: 5px; top: 533px; width: 528px; height: 312px; }
  .envelope-body {
    position: absolute; left: 0; top: 72px; width: 528px; height: 240px;
    border: 10px solid var(--green); background: var(--paper);
  }
  .envelope-flap { position: absolute; left: 0; top: 0; }
  .envelope-to { position: absolute; left: 40px; top: 128px; font-size: 9px; }
  .envelope-lines { position: absolute; left: 52px; top: 142px; width: 160px; }
  .envelope-lines span { display: block; height: 1px; background: var(--blue); margin-bottom: 18px; }
  .envelope .brand-dot { position: absolute; left: 440px; top: 110px; width: 28px; height: 28px; }
  .envelope-rule { position: absolute; left: 18px; right: 18px; top: 238px; height: 1px; background: var(--blue); }
  .return-address {
    position: absolute; right: 20px; top: 244px; text-align: right;
    font-size: 8px; line-height: 1.55; color: var(--blue); white-space: nowrap;
  }

  /* Letterhead */
  .letterhead {
    position: absolute; left: 600px; top: 5px; width: 595px; height: 847px;
    border: 12px solid var(--green); background: var(--paper);
  }
  .letterhead .brand { position: absolute; left: 20px; top: 36px; font-size: 18px; }
  .letterhead .brand-dot { width: 28px; height: 28px; }
  .letterhead-rule { position: absolute; left: 17px; right: 11px; height: 1px; background: var(--blue); }
  .letterhead-rule.top { top: 108px; }
  .letterhead-rule.bottom { top: 746px; }
  .letterhead-mark { position: absolute; left: 20px; top: 490px; }
  .letterhead-address {
    position: absolute; right: 11px; top: 762px; text-align: right;
    font-size: 8px; line-height: 1.7; color: var(--blue); white-space: nowrap;
  }
</style>
</head>
<body>

  <section class="card-front">
    <div class="brand"><span class="brand-dot"></span>Brightwave Home Services</div>
  </section>

  <section class="card-back">
    <div class="card-back-contact">
      <p>4200 Maple Crest Drive, Suite 210,</p>
      <p>Raleigh NC, 27609</p>
      <p>www.brightwavehomeservices.example</p>
      <p>Name@brightwavehomeservices.example</p>
    </div>
    <div class="card-back-name">
      <p>Brightwave Home Services</p>
      <p>(919) 555-0142</p>
    </div>
  </section>

  <section class="envelope">
    <div class="envelope-body"></div>
    <svg class="envelope-flap" width="528" height="135" viewBox="0 0 528 135" aria-hidden="true">
      <defs>
        <linearGradient id="flap-fill" x1="0" y1="0" x2="0" y2="1">
          <stop offset="0" stop-color="#1aa3e8"/>
          <stop offset="1" stop-color="#ffffff"/>
        </linearGradient>
      </defs>
      <path d="M0 0 H528 V72 L264 135 L0 72 Z" fill="url(#flap-fill)"/>
    </svg>
    <p class="envelope-to">To:</p>
    <div class="envelope-lines"><span></span><span></span><span></span><span></span></div>
    <span class="brand-dot"></span>
    <div class="envelope-rule"></div>
    <div class="return-address">
      <p>4200 Maple Crest Drive, Suite 210,</p>
      <p>Raleigh NC, 27609</p>
      <p>www.brightwavehomeservices.example &nbsp;|&nbsp; Name@brightwavehomeservices.example</p>
    </div>
  </section>

  <section class="letterhead">
    <div class="brand"><span class="brand-dot"></span>Brightwave Home Services</div>
    <div class="letterhead-rule top"></div>
    <svg class="letterhead-mark" width="220" height="220" viewBox="0 0 220 220" aria-hidden="true">
      <defs>
        <radialGradient id="mark-fill" cx="0.5" cy="0.45" r="0.55">
          <stop offset="0" stop-color="#bfe6fa" stop-opacity="0.8"/>
          <stop offset="1" stop-color="#bfe6fa" stop-opacity="0.25"/>
        </radialGradient>
      </defs>
      <circle cx="110" cy="110" r="100" fill="url(#mark-fill)"/>
    </svg>
    <div class="letterhead-rule bottom"></div>
    <div class="letterhead-address">
      <p>4200 Maple Crest Drive, Suite 210,</p>
      <p>Raleigh NC, 27609</p>
      <p>www.brightwavehomeservices.example &nbsp;|&nbsp; Name@brightwavehomeservices.example</p>
    </div>
  </section>

</body>
</html>
```